LQV Web Site

Build a web site for Distant Charting and Rostering (LQV)

Target Market(s)

Petrochemical, Refining, and Manufacturing

Industry/Entity Type

Manufacturing

Coding

Coded - Design and coding required

Number of Pages Required

1 page

Font styles to use
Sans Serif

Colors

Designer to choose only greyscale colors for use in the design.

Requirements
Must have
• LQV is a member of WEN Venture Services family of companies, along with Brivonta, and Mulvarde.
Would like LQV to mimic Brivonta, and Mulvarde in layout and functionality.
WIll use the same office address and phone # found Brivonta and Mulvarde.
The color scheme needs to match the logo colors.
The final product needs to be in word press.
would like to connect the QR code found on one-pager to the website.

Reference these websites: www.brivonta-example.com and www.mulvarde-example.com
Nice to have
• Would like to have a contact tab similar to the one found on Mulvarde website. Use this email address. (LQV@WEN.example.com)
The home page needs to have simple depictions of the problem statement, solution, and introduction to LQV. (use the video script to help, feel free to use your own words)

```html
<!DOCTYPE html>
<html lang="en">
<head>
<meta charset="utf-8">
<title>LQV – Distant Charting and Rostering</title>
<link href="https://fonts.googleapis.com/css2?family=Bebas+Neue&family=Barlow+Condensed:wght@300;400;500&family=Poppins:wght@400;500;600&display=swap" rel="stylesheet">
<style>
:root{
  --blue:#3b9ad8;
  --blue-deep:#2d86c4;
  --blue-band:#3a98d6;
  --ink:#1f2024;
  --dark:#232428;
  --text:#333;
  --muted:#6a6a6a;
  --white:#fff;
  --line:#c9ccd1;
}
*{margin:0;padding:0;box-sizing:border-box}
html,body{width:1200px;height:4732px;overflow:hidden}
body{position:relative;background:var(--white);font-family:"Poppins",sans-serif;color:var(--text)}
.abs{position:absolute}
.heading{font-family:"Bebas Neue",sans-serif;font-weight:400;letter-spacing:1px}
.rule{position:absolute;height:3px;background:var(--blue);width:54px}
.btn{position:absolute;display:flex;align-items:center;justify-content:center;background:var(--blue);color:var(--white);border-radius:26px;font-family:"Poppins",sans-serif;font-weight:500;font-size:17px;box-shadow:0 4px 10px rgba(0,0,0,.18)}

/* hero */
.hero{position:absolute;left:0;top:0;width:1200px;height:710px;clip-path:polygon(0 0,1200px 0,1200px 643px,600px 708px,0 643px);
  background:linear-gradient(180deg,#3b3a55 0%,#6b5a78 22%,#a67f7b 36%,#4b5566 55%,#8a8f98 75%,#5c6470 100%)}
.hero-chevron{position:absolute;left:423px;top:717px}
.brand{position:absolute;display:flex;align-items:center;gap:12px;color:var(--blue)}
.brand .dot{width:22px;height:22px;border-radius:50%;background:var(--blue)}
.brand .name{font-family:"Bebas Neue",sans-serif;font-size:64px;line-height:1;letter-spacing:3px}
.brand .sub{font-family:"Poppins",sans-serif;font-size:10px;letter-spacing:.5px;margin-top:2px}
.nav{position:absolute;top:57px;left:0;font-family:"Barlow Condensed",sans-serif;font-size:15px;color:var(--white);letter-spacing:.5px}
.nav span{position:absolute;white-space:nowrap}
.nav .active::after{content:"";position:absolute;left:0;right:0;top:24px;height:3px;background:var(--blue)}
.hero-title{position:absolute;left:0;width:1200px;top:305px;text-align:center;font-family:"Bebas Neue",sans-serif;font-size:62px;color:var(--white);letter-spacing:2px;text-shadow:0 2px 6px rgba(0,0,0,.4)}
.arrow{position:absolute;width:80px;height:80px;border:2px solid rgba(255,255,255,.85);border-radius:50%}
.dots{position:absolute;top:638px;left:578px;display:flex;gap:8px}
.dots i{width:6px;height:6px;border-radius:50%;background:#fff}
.dots i:first-child{background:var(--blue)}

/* about */
.about-visual{position:absolute;left:132px;top:836px;width:410px;height:395px;border-radius:18px;background:linear-gradient(135deg,#4b79c2 0%,#6b8ab1 40%,#8c929c 100%)}
.about-title{left:663px;top:838px;font-size:40px;color:var(--ink)}
.about-sub{left:661px;top:884px;font-family:"Barlow Condensed",sans-serif;font-weight:300;font-size:30px;color:var(--blue)}
.about-text{left:663px;top:948px;width:430px;font-size:14px;line-height:25.8px;color:var(--text);font-weight:500}

/* problem */
.problem{position:absolute;left:0;top:1314px;width:1200px;height:739px;clip-path:polygon(0 92px,600px 0,1200px 92px,1200px 629px,600px 739px,0 629px);
  background:linear-gradient(180deg,rgba(59,154,216,.93),rgba(45,134,196,.95)),linear-gradient(90deg,#2f6f9c,#4b8fbe)}
.problem-title{left:0;width:1200px;text-align:center;top:1420px;font-size:44px;color:var(--white)}
.orbit{position:absolute;left:426px;top:1523px;width:350px;height:350px;border:3px dotted rgba(255,255,255,.9);border-radius:50%}
.core{position:absolute;left:486px;top:1583px;width:230px;height:230px;border-radius:50%;background:#fff;display:flex;align-items:center;justify-content:center}
.core-inner{width:206px;height:206px;border-radius:50%;background:radial-gradient(circle at 50% 40%,#4b5766,#1e232a);display:flex;align-items:center;justify-content:center;font-family:"Bebas Neue",sans-serif;font-size:52px;color:var(--blue);letter-spacing:3px}
.node{position:absolute;width:62px;height:62px;border-radius:50%;background:#fff;display:flex;align-items:center;justify-content:center}
.issue{position:absolute;font-size:16px;line-height:26px;font-weight:600;color:var(--white)}
.issue.right{text-align:right}

/* cards */
.card{position:absolute;top:2140px;width:311px;height:461px;background:#fff;box-shadow:0 2px 12px rgba(0,0,0,.16);border-radius:4px;text-align:center}
.card .photo{margin:6px 7px 0;height:182px}
.card h3{font-family:"Barlow Condensed",sans-serif;font-weight:500;font-size:27px;color:var(--blue);margin-top:34px;letter-spacing:.5px}
.card p{font-size:13.5px;line-height:23px;color:var(--text);padding:0 22px;margin-top:6px;height:116px;overflow:hidden}
.card .more{display:inline-block;margin-top:16px;font-size:12px;font-weight:600;color:var(--blue);border-bottom:1px solid var(--blue)}

/* how it works */
.how{position:absolute;left:0;top:2702px;width:1200px;height:735px;clip-path:polygon(0 83px,600px 0,1200px 83px,1200px 625px,600px 735px,0 625px)}
.how .dark{position:absolute;left:0;top:0;width:600px;height:735px;background:var(--dark)}
.how .photo{position:absolute;left:600px;top:0;width:600px;height:735px;background:linear-gradient(160deg,#4d7fb6 0%,#8fb1d0 30%,#c9a43a 55%,#8a6a1e 78%,#2b4a69 100%)}
.how-title{left:112px;top:2856px;font-size:42px;color:var(--white)}
.how-text{left:112px;top:2936px;width:430px;font-size:14.3px;line-height:25.8px;color:var(--white);font-weight:500}

/* contact */
.contact-title{left:0;width:1200px;text-align:center;top:3515px;font-size:44px;color:var(--ink)}
.c-icon{position:absolute;left:112px;width:56px;height:56px;border:2px solid var(--blue);border-radius:50%;display:flex;align-items:center;justify-content:center}
.c-label{position:absolute;left:195px;font-family:"Barlow Condensed",sans-serif;font-weight:500;font-size:18px;color:var(--blue)}
.c-value{position:absolute;left:196px;font-size:18px;line-height:25.5px;color:var(--ink);font-weight:500}
.field{position:absolute;border:1.5px solid var(--line);background:#fff;display:flex;align-items:center;padding-left:18px;gap:12px;font-size:14.5px;color:#666}
.field.msg{align-items:flex-start;padding-top:16px}

/* footer */
.footer{position:absolute;left:0;top:4125px;width:1200px;height:607px;background:var(--dark);clip-path:polygon(0 85px,600px 0,1200px 85px,1200px 607px,0 607px)}
.foot-head{position:absolute;top:4285px;font-family:"Barlow Condensed",sans-serif;font-weight:500;font-size:19px;color:var(--white);letter-spacing:.5px}
.foot-list{position:absolute;top:4330px;list-style:none;font-size:13px;line-height:24.5px;color:#b8bcc2}
.foot-list li::before{content:"";display:inline-block;width:5px;height:5px;border-radius:50%;background:var(--blue);margin-right:16px;vertical-align:middle}
.social{position:absolute;top:4424px;width:48px;height:48px;border-radius:50%;background:var(--blue)}
.partner{position:absolute;top:4556px;font-family:"Poppins",sans-serif;font-weight:600;font-size:30px;line-height:1;color:#d7dadf}
.legal{position:absolute;top:4630px;font-size:12px;color:#9ea3aa}
</style>
</head>
<body>

<!-- Hero -->
<section class="hero" role="img" aria-label="Refinery at dusk with storage tanks and process towers"></section>
<svg class="hero-chevron" width="358" height="42" viewBox="0 0 358 42"><polygon points="0,0 179,40 358,0 179,22" fill="var(--blue)"/></svg>

<div class="brand" style="left:114px;top:20px">
  <span class="dot"></span>
  <div><div class="name">LQV</div><div class="sub">DISTANT CHARTING AND ROSTERING</div></div>
</div>
<nav class="nav">
  <span class="active" style="left:465px">HOME</span>
  <span style="left:546px">ABOUT US</span>
  <span style="left:654px">SERVICES</span>
  <span style="left:763px">SUPPORT</span>
  <span style="left:868px">COMMUNICATIONS</span>
  <span style="left:1029px">CONTACT</span>
</nav>
<h1 class="hero-title">DISTANT CHARTING AND ROSTERING</h1>
<div class="btn" style="left:496px;top:410px;width:206px;height:50px">GIVE WEN A CALL</div>
<div class="arrow" style="left:8px;top:318px"><svg width="76" height="76" viewBox="0 0 76 76"><polyline points="42,28 32,38 42,48" fill="none" stroke="#fff" stroke-width="3"/></svg></div>
<div class="arrow" style="left:1111px;top:318px"><svg width="76" height="76" viewBox="0 0 76 76"><polyline points="34,28 44,38 34,48" fill="none" stroke="#fff" stroke-width="3"/></svg></div>
<div class="dots"><i></i><i></i><i></i><i></i></div>

<!-- About -->
<div class="about-visual" role="img" aria-label="Technicians working on plant piping, framed in a large letter shape"></div>
<h2 class="abs heading about-title">ABOUT</h2>
<div class="abs about-sub">DISTANT CHARTING AND ROSTERING</div>
<div class="rule" style="left:663px;top:932px"></div>
<p class="abs about-text">Sed ut perspiciatis unde omnis iste natus error sit voluptatem accusantium doloremque laudantium, totam rem aperiam, eaque ipsa quae ab illo inventore veritatis et quasi architecto beatae vitae dicta sunt explicabo. Nemo enim ipsam voluptatem quia voluptas sit aspernatur aut odit aut fugit, sed quia consequuntur magni dolores eos qui ratione voluptatem sequi nesciunt. Neque porro quisquam est, qui dolorem ipsum quia dolor sit amet,</p>
<div class="btn" style="left:663px;top:1182px;width:177px;height:50px">READ MORE</div>

<!-- Problem -->
<section class="problem" role="img" aria-label="Faint aerial view of a refinery under a blue overlay"></section>
<h2 class="abs heading problem-title">PROBLEM</h2>
<div class="rule" style="left:573px;top:1489px;background:#fff"></div>
<div class="orbit"></div>
<div class="core"><div class="core-inner">LQV</div></div>

<div class="node" style="left:397px;top:1649px"><svg width="30" height="30" viewBox="0 0 30 30" fill="none" stroke="var(--blue)" stroke-width="2"><circle cx="15" cy="10" r="5"/><path d="M5 27c0-6 4-10 10-10s10 4 10 10"/></svg></div>
<div class="node" style="left:737px;top:1649px"><svg width="30" height="30" viewBox="0 0 30 30" fill="none" stroke="var(--blue)" stroke-width="2"><path d="M3 27V14l7 4v-4l7 4V6h5v21z"/></svg></div>
<div class="node" style="left:425px;top:1794px"><svg width="30" height="30" viewBox="0 0 30 30" fill="none" stroke="var(--blue)" stroke-width="2"><rect x="5" y="5" width="20" height="20"/><path d="M5 12h20M12 12v13"/></svg></div>
<div class="node" style="left:708px;top:1794px"><svg width="30" height="30" viewBox="0 0 30 30" fill="none" stroke="var(--blue)" stroke-width="2"><path d="M4 26h22M7 26V10h6v16M17 26V4h6v22"/></svg></div>

<div class="issue right" style="left:62px;width:300px;top:1654px">Legal liabilities, co-employment<br>issues</div>
<div class="issue" style="left:831px;top:1654px">High cost for turnaround planning<br>and scheduling</div>
<div class="issue right" style="left:97px;width:300px;top:1805px">Distraction due to plant<br>upsets, or site interferences</div>
<div class="issue" style="left:792px;top:1805px">Safety risks, social distancing<br>issues</div>

<!-- Cards -->
<article class="card" style="left:110px">
  <div class="photo" role="img" aria-label="Two workers in hard hats at a refinery" style="background:linear-gradient(160deg,#7aa3cf,#3e5f86 60%,#c9b56a)"></div>
  <h3>GENERAL SOLUTION</h3>
  <p>A customizable solution that you pay for one time. That reduces the owner's risk, is not impacted by site conditions or limitations, is transparent, and accountable for planning and scheduling turnarounds.</p>
  <span class="more">READ MORE</span>
</article>
<article class="card" style="left:445px">
  <div class="photo" role="img" aria-label="Engineer holding rolled plans with a hard hat, plant at sunset" style="background:linear-gradient(160deg,#e8e2da,#d9a870 50%,#f0c27a)"></div>
  <h3>INTRODUCE PRODUCT</h3>
  <p>Distant Charting and Rostering is a new way of providing the same process of developing job plans, work packages, and turnaround schedules for a fraction of the cost of conventional methods.</p>
  <span class="more">READ MORE</span>
</article>
<article class="card" style="left:779px">
  <div class="photo" role="img" aria-label="Lit refinery towers against a cloudy sky" style="background:linear-gradient(180deg,#8e97a3,#5a6069 50%,#c9874a)"></div>
  <h3>HOW IT WORKS (GENERAL)</h3>
  <p>LQV still follows all the industry rules for planning and scheduling. But we now are able to perform a large portion of the processes off-site / remotely. By doing this reduces cost, minimizes client's exposer to legal liabilities, and</p>
  <span class="more">READ MORE</span>
</article>

<!-- How it works -->
<section class="how">
  <div class="dark"></div>
  <div class="photo" role="img" aria-label="Yellow offshore production platform with cranes and flare stacks"></div>
</section>
<h2 class="abs heading how-title">HOW IT WORKS (SPECIFIC)</h2>
<div class="rule" style="left:112px;top:2911px"></div>
<p class="abs how-text">How LQV works: An onsite team is to collects all the necessary information required to develop job plans. Then share it with the remote team using a planning software that both sides can access. The remote team then uses the information and documents to establish job plans and work packages. A scheduler can then develop a turnaround schedule from the completed job plans from WEN's office, where WEN's management staff can monitor, manage, and provide expert guidance to the team. By using current</p>
<div class="btn" style="left:112px;top:3202px;width:177px;height:50px">READ MORE</div>

<!-- Contact -->
<h2 class="abs heading contact-title">CONTACT US</h2>
<div class="rule" style="left:573px;top:3572px"></div>

<div class="c-icon" style="top:3615px"><svg width="24" height="24" viewBox="0 0 24 24"><path d="M6 2l4 4-2 3c1 3 4 6 7 7l3-2 4 4-3 4C10 22 2 14 2 5z" fill="var(--ink)"/></svg></div>
<div class="c-label" style="top:3613px">PHONE</div>
<div class="c-value" style="top:3636px">555 010 4575</div>

<div class="c-icon" style="top:3740px"><svg width="24" height="24" viewBox="0 0 24 24" fill="none" stroke="var(--ink)" stroke-width="2"><rect x="2" y="5" width="20" height="14"/><path d="M2 5l10 8 10-8"/></svg></div>
<div class="c-label" style="top:3738px">EMAIL</div>
<div class="c-value" style="top:3761px">LQV@WEN.example.com</div>

<div class="c-icon" style="top:3861px"><svg width="24" height="24" viewBox="0 0 24 24"><path d="M12 1a8 8 0 0 0-8 8c0 6 8 14 8 14s8-8 8-14a8 8 0 0 0-8-8zm0 11a3 3 0 1 1 0-6 3 3 0 0 1 0 6z" fill="var(--ink)"/></svg></div>
<div class="c-label" style="top:3855px">ADDRESS</div>
<div class="c-value" style="top:3879px">18 Harlow Lane,<br>Fenmoor,<br>CA, 90000, USA</div>

<div class="field" style="left:445px;top:3613px;width:312px;height:52px"><svg width="14" height="14" viewBox="0 0 14 14" fill="var(--blue)"><circle cx="7" cy="4" r="3.5"/><path d="M0 14c0-4 3-6 7-6s7 2 7 6z"/></svg>First Name</div>
<div class="field" style="left:772px;top:3613px;width:314px;height:52px"><svg width="14" height="14" viewBox="0 0 14 14" fill="var(--blue)"><circle cx="7" cy="4" r="3.5"/><path d="M0 14c0-4 3-6 7-6s7 2 7 6z"/></svg>Last Name</div>
<div class="field" style="left:445px;top:3691px;width:312px;height:52px"><svg width="15" height="12" viewBox="0 0 15 12" fill="none" stroke="var(--blue)" stroke-width="1.5"><rect x="1" y="1" width="13" height="10"/><path d="M1 1l6.5 5L14 1"/></svg>Email</div>
<div class="field" style="left:772px;top:3691px;width:314px;height:52px"><svg width="14" height="14" viewBox="0 0 24 24"><path d="M6 2l4 4-2 3c1 3 4 6 7 7l3-2 4 4-3 4C10 22 2 14 2 5z" fill="var(--blue)"/></svg>Phone</div>
<div class="field msg" style="left:445px;top:3768px;width:641px;height:176px"><svg width="14" height="14" viewBox="0 0 14 14"><path d="M1 1l12 12" stroke="var(--blue)" stroke-width="2"/></svg>Message</div>
<div class="btn" style="left:445px;top:3964px;width:176px;height:50px">SUBMIT</div>

<!-- Footer -->
<svg class="abs" style="left:423px;top:4100px" width="358" height="46" viewBox="0 0 358 46"><polygon points="0,44 179,0 358,44 179,24" fill="var(--blue)"/></svg>
<footer class="footer"></footer>

<div class="brand" style="left:125px;top:4276px">
  <span class="dot"></span>
  <div><div class="name">LQV</div><div class="sub">DISTANT CHARTING AND ROSTERING</div></div>
</div>
<span class="social" style="left:132px" aria-label="Social link"></span>
<span class="social" style="left:193px" aria-label="Social link"></span>
<span class="social" style="left:250px" aria-label="Social link"></span>
<span class="social" style="left:309px" aria-label="Social link"></span>

<div class="foot-head" style="left:434px">QUICK LINKS</div>
<ul class="foot-list" style="left:434px">
  <li>HOME</li><li>ABOUT US</li><li>SERVICES</li><li>SUPPORT</li><li>COMMUNICATIONS</li><li>CONTACT</li>
</ul>
<div class="foot-head" style="left:627px">CONTACT US</div>
<ul class="foot-list" style="left:627px">
  <li>FAQ</li><li>TERMS &amp; CONDITIONS</li><li>PRIVACY POLICY</li><li>SITE MAP</li>
</ul>
<div class="foot-head" style="left:836px">NEWSLETTER</div>
<p class="abs" style="left:836px;top:4332px;width:255px;font-size:12.5px;line-height:20px;color:#b8bcc2">Reach us today to get all latest updates, News &amp; to get resources on how to attract &amp; retain more</p>
<div class="abs" style="left:836px;top:4415px;width:250px;height:42px;border-radius:21px;background:#fff;display:flex;align-items:center;padding-left:20px;gap:8px;font-size:12.5px;color:#777"><svg width="15" height="12" viewBox="0 0 15 12" fill="none" stroke="#777" stroke-width="1.3"><rect x="1" y="1" width="13" height="10"/><path d="M1 1l6.5 5L14 1"/></svg>Enter E-Mail</div>
<div class="btn" style="left:836px;top:4475px;width:118px;height:37px;font-size:12px">SUBMIT</div>

<div class="partner" style="left:330px">Mulvarde</div>
<div class="partner" style="left:600px">Brivonta</div>
<div class="partner" style="left:814px">WEN</div>

<div class="abs" style="left:1114px;top:4586px;width:36px;height:36px;border-radius:50%;background:var(--blue)"><svg width="36" height="36" viewBox="0 0 36 36"><polyline points="13,20 18,15 23,20" fill="none" stroke="#fff" stroke-width="2"/></svg></div>

<div class="legal" style="left:110px">© 2021 Distant Charting and Rostering - All rights reserved</div>
<div class="legal" style="left:833px">Terms &amp; Conditions</div>
<div class="abs" style="left:978px;top:4622px;width:1px;height:28px;background:#6d7178"></div>
<div class="legal" style="left:1002px">Privacy Policy</div>

</body>
</html>
```